Marrowgate Auctions Business Cards Design Needed

I need a business card design that is modern looking - double sided (maybe just my logo on the back, but open to suggestions) - the overall design is up to you. I want it to be easy to read - not over the top flashy. I already have a company logo which I uploaded so that needs to be used. The colors of my logo are the colors I want on the card... so blue and gray (do need to match the logo colors).

Requirements
Must have
• Would like the card to be sleek, modern and easy to ready

```html
<!DOCTYPE html>
<html lang="en">
<head>
<meta charset="UTF-8">
<title>Marrowgate Auctions Business Cards</title>
<link href="https://fonts.googleapis.com/css2?family=Lato:wght@400;700;900&family=Michroma&display=swap" rel="stylesheet">
<style>
  :root {
    --backdrop: #e4e7eb;
    --card-light: #ffffff;
    --card-mid: #f4f6f8;
    --card-dark: #e2e6ea;
    --brand-blue: #1f4e8c;
    --ink-gray: #4a525c;
    --rule-gray: #8a939e;
  }
  * { margin: 0; padding: 0; box-sizing: border-box; }
  html, body { width: 1200px; height: 900px; overflow: hidden; }
  body {
    background: var(--backdrop);
    position: relative;
    font-family: "Lato", sans-serif;
    color: var(--ink-gray);
  }
  .card {
    position: absolute;
    background: radial-gradient(ellipse at 30% 10%, var(--card-light) 0%, var(--card-mid) 55%, var(--card-dark) 100%);
    box-shadow: 3px 4px 8px rgba(40, 50, 60, 0.35);
    text-align: center;
  }
  .card-front { left: 330px; top: 90px; width: 555px; height: 343px; }
  .card-back { left: 330px; top: 470px; width: 558px; height: 342px; }

  .holder-name {
    font-family: "Michroma", sans-serif;
    font-weight: 400;
    font-size: 20px;
    line-height: 25px;
    letter-spacing: 0.5px;
    color: var(--brand-blue);
    margin-top: 94px;
  }
  .holder-title { font-size: 17px; line-height: 20px; margin-top: 3px; }

  .contact-divider {
    display: flex;
    justify-content: center;
    align-items: center;
    gap: 4px;
    margin-top: 18px;
  }
  .contact-divider .rule { width: 56px; height: 1px; background: var(--rule-gray); }
  .contact-divider .rule.left { margin-right: 2px; }
  .contact-divider .rule.right { margin-left: 2px; }
  .contact-icon { width: 17px; height: 17px; display: block; }

  .contact-list { margin-top: 9px; font-size: 16px; line-height: 20px; }

  .brand-mark {
    display: block;
    width: 80px;
    height: 80px;
    margin: 92px auto 0;
    background: var(--brand-blue);
  }
  .brand-name {
    font-weight: 900;
    font-size: 33px;
    line-height: 40px;
    letter-spacing: 0.5px;
    color: var(--brand-blue);
    margin-top: 12px;
  }
  .tagline {
    font-size: 14px;
    letter-spacing: 0.3px;
    margin-top: 17px;
  }
</style>
</head>
<body>
  <section class="card card-front">
    <h1 class="holder-name">COLIN HARTWELL</h1>
    <p class="holder-title">Owner/President - Auctioneer</p>
    <div class="contact-divider">
      <span class="rule left"></span>
      <svg class="contact-icon" viewBox="0 0 17 17" aria-label="Phone">
        <rect width="17" height="17" fill="#1f4e8c"/>
        <path d="M4 7 Q8.5 3 13 7 L11.5 8.5 L10 7.2 L7 7.2 L5.5 8.5 Z M5 10 h7 v3 h-7 z" fill="#ffffff"/>
      </svg>
      <svg class="contact-icon" viewBox="0 0 17 17" aria-label="Email">
        <rect width="17" height="17" fill="#1f4e8c"/>
        <rect x="3.5" y="5" width="10" height="7" fill="none" stroke="#ffffff" stroke-width="1.2"/>
        <path d="M3.5 5 L8.5 9 L13.5 5" fill="none" stroke="#ffffff" stroke-width="1.2"/>
      </svg>
      <svg class="contact-icon" viewBox="0 0 17 17" aria-label="Website">
        <rect width="17" height="17" fill="#1f4e8c"/>
        <circle cx="8.5" cy="8.5" r="4.8" fill="none" stroke="#ffffff" stroke-width="1.2"/>
        <path d="M3.7 8.5 h9.6 M8.5 3.7 q-3 4.8 0 9.6 M8.5 3.7 q3 4.8 0 9.6" fill="none" stroke="#ffffff" stroke-width="1"/>
      </svg>
      <span class="rule right"></span>
    </div>
    <div class="contact-list">
      <p>555-310-4827</p>
      <p>marrowgatebids@example.com</p>
      <p>http://gavelrevival.com/</p>
    </div>
  </section>

  <section class="card card-back">
    <span class="brand-mark" aria-hidden="true"></span>
    <h2 class="brand-name">MARROWGATE AUCTIONS</h2>
    <p class="tagline">IMPROVING CHARITY AUCTIONS NATIONWIDE</p>
  </section>
</body>
</html>
```